Velder Auto Repair - Flyer Design

My business is a automobile shop where we fix cars. Such things that we do but not limited to is brakes, Engine/Transmission change, Electrical work, emission test, oil change and automobile diagnostic. I am looking for a flyer that will catch peoples attention, I will be giving flyers to people, putting them in car windows and mailboxes. I am looking for a flier that will help to attract more customers to my business. I also want the flyer to say "Bring in your estimate from our competitors with this flyer and we will beat it by 10%" (does not have to be in those exact words). I also want the flyer to have my business address phone and operating hours. I have attached a business card and my business ad which I have placed in the newspaper before. I hope it helps with your design.
Industry/Entity Type
Car Repair
Look and feel

```html
<!DOCTYPE html>
<html lang="en">
<head>
<meta charset="utf-8">
<title>Velder Auto Repair – Flyer</title>
<link href="https://fonts.googleapis.com/css2?family=Alfa+Slab+One&family=Oswald:wght@400;500&family=Roboto+Condensed:wght@400;700&display=swap" rel="stylesheet">
<style>
  :root {
    --bg: #e9e6e2;
    --red: #e2171f;
    --black: #141414;
    --white: #f2f2f2;
    --grey: #bdbdbd;
  }
  * { margin: 0; padding: 0; box-sizing: border-box; }
  html, body { width: 1200px; height: 1200px; overflow: hidden; background: var(--bg); }
  .flyer {
    position: absolute; left: 50px; top: 365px;
    width: 1100px; height: 470px;
    display: flex; background: var(--black);
    box-shadow: 0 6px 18px rgba(0,0,0,.25);
    overflow: hidden;
  }
  .offer {
    flex: none; width: 330px; height: 100%; background: var(--red); color: var(--white);
    font-family: "Oswald", sans-serif; text-transform: uppercase;
    padding: 26px 18px 0 36px;
  }
  .offer__lead { font-size: 33px; line-height: 1.2; font-weight: 500; white-space: nowrap; }
  .offer__value {
    font-family: "Alfa Slab One", serif; font-size: 112px; line-height: 1;
    margin: 10px 0 0 -10px; white-space: nowrap;
  }
  .offer__tail { font-size: 33px; font-weight: 500; margin-top: 6px; white-space: nowrap; }
  .info {
    flex: none; position: relative; width: 420px; height: 100%;
    padding: 24px 20px 0 34px; color: var(--white);
  }
  .brand {
    font-family: "Alfa Slab One", serif; font-size: 40px; line-height: 1.1; font-weight: 400;
    color: var(--white); text-transform: uppercase; text-align: right; white-space: nowrap;
  }
  .contact { list-style: none; margin-top: 10px; font-family: "Roboto Condensed", sans-serif; font-weight: 700; font-size: 19px; line-height: 1.2; }
  .contact li { display: flex; gap: 10px; align-items: flex-start; }
  .contact svg { flex: none; margin-top: 4px; }
  .specialty { margin-top: 16px; font-family: "Oswald", sans-serif; font-size: 28px; line-height: 1.2; text-transform: uppercase; font-weight: 500; }
  .specialty small { font-size: 15px; }
  .services { margin-top: 12px; font-family: "Roboto Condensed", sans-serif; font-weight: 700; font-size: 15px; line-height: 1.25; }
  .hours { margin-top: 12px; font-family: "Oswald", sans-serif; font-size: 15px; color: var(--grey); white-space: nowrap; }
  .photo {
    flex: 1; height: 100%;
    background: linear-gradient(160deg, #e8e8e8 0%, #8a8a8a 30%, #1a1a1a 55%, #d8d8d8 85%, #f0f0f0 100%);
  }
</style>
</head>
<body>
  <article class="flyer">
    <section class="offer">
      <p class="offer__lead">Bring in your<br>estimate from<br>our competitors<br>with this flyer<br>and you will get</p>
      <p class="offer__value">10%</p>
      <p class="offer__tail">Discount on it !!!</p>
    </section>
    <section class="info">
      <h1 class="brand">Velder Auto<br>Repair</h1>
      <ul class="contact">
        <li><svg width="14" height="14" viewBox="0 0 14 14"><circle cx="7" cy="7" r="5.5" fill="none" stroke="currentColor" stroke-width="2.5"/></svg><span>2450 W Harbor Ave.<br>Millbrook IL. 60499</span></li>
        <li><svg width="14" height="14" viewBox="0 0 14 14"><path d="M3 1l3 3-2 2a8 8 0 0 0 4 4l2-2 3 3-2 2C6 13 1 8 1 3z" fill="currentColor"/></svg><span>(555) 014-2278</span></li>
        <li><svg width="14" height="14" viewBox="0 0 14 14"><text x="0" y="12" font-size="13" fill="currentColor" font-family="sans-serif">@</text></svg><span>VelderAutoRepair@mail.com</span></li>
      </ul>
      <h2 class="specialty">Specializing in<br>Foreign <small>&amp;</small> Domestic cars</h2>
      <p class="services">Offer includes but is not limited to: brakes, engine/transmission change, electrical work, emission test, oil change and automobile diagnostic ...</p>
      <p class="hours">Hours: Mon.-Fri. 8am-5pm; Sat. 8am-4pm; Sun. Closed</p>
    </section>
    <div class="photo" role="img" aria-label="High-contrast black and white photo of a mechanic working on a car engine"></div>
  </article>
</body>
</html>
```